Wholesale company needs a sales brochure for our latest gadget- Orbo Tag. We sell to retailers

We need a sale brochure for our new product- Orbo/Velt Tag. It's an elegant little device that connects to any smartphone using an APP and let you locate your keys or your phone when you can't find them. We would like to see a design that uses the colors: Light blue, Black and metallic silver. The final design should communicate tech and innovative product. We need a total of 4 pages of 8.5x11'' (US letter size) to describe:
- Product benefits
- Product in use
- Display solution
- Profit generator
- Success story

Attached below are photos of the packaging and the display for your reference. Better photos will be sent later.
Please keep in mind that this product should be displayed on the counter with high foot traffic OR hang on hooks on a display fixture in the store.

This brochure will be used mainly to be sent digitally via email BUT we will also print it and will be mailing copies to our buyers.

Target Market(s)

Retailers and Distributors.
Small to mid-size retail stores:
- Electronic stores
- Convenient store
- Cellphone stores
- Gift stores

Industry/Entity Type

Retail

Font styles to use
Sans Serif

Colors
0692cd
ffffff
f3f1f8
33a6d7
85cae6

Requirements
Must have
• Must have:
• - "techie" and innovative look to go hand in hand with the product itself.
• - "in use" photos
• - "Description of the product"
• - Spec info
Nice to have
• Pattern or abstract design on background behind the text and images

```html
<!DOCTYPE html>
<html lang="en">
<head>
<meta charset="utf-8">
<title>Orbo Tag Brochure – Features &amp; Application</title>
<link href="https://fonts.googleapis.com/css2?family=Open+Sans:wght@400;600;700&family=Oswald:wght@300;400&display=swap" rel="stylesheet">
<style>
  :root{
    --blue:#33a6d7;
    --blue-deep:#0692cd;
    --blue-soft:#85cae6;
    --blue-faint:#d6ebf5;
    --ink:#1b1b1b;
    --paper:#ffffff;
    --mist:#f3f1f8;
    --wood:#8a5a36;
  }
  *{box-sizing:border-box;margin:0;padding:0}
  html,body{width:1200px;height:434px;overflow:hidden;background:var(--paper)}
  body{font-family:"Open Sans",Arial,sans-serif;color:var(--ink)}
  .spread{position:relative;width:1200px;height:434px;display:flex}
  .page{position:relative;width:600px;height:434px;overflow:hidden;background:var(--paper)}
  .page svg.bg{position:absolute;inset:0}

  /* Features page */
  .feature-number{position:absolute;font-family:"Oswald",Arial,sans-serif;font-weight:400;font-size:58px;color:var(--blue-faint);line-height:1}
  .feature-icon{position:absolute}
  .feature-title{position:absolute;font-weight:700;font-size:17px;white-space:nowrap}
  .feature-rule{position:absolute;height:2px;background:var(--blue-soft)}
  .feature-text{position:absolute;font-size:11px;line-height:1.3;color:var(--blue)}
  .page-heading{position:absolute;font-family:"Oswald",Arial,sans-serif;font-weight:300;color:var(--paper);letter-spacing:3px;line-height:1}
  .features-heading{right:100px;bottom:40px;font-size:44px}

  /* Application page */
  .application-heading{left:14px;top:44px;font-size:44px}
  .setup{position:absolute;right:14px;top:30px;width:220px;text-align:right}
  .setup h2,.finding h2{font-size:13px;font-weight:700;margin-bottom:6px}
  .setup ol{list-style:none;font-size:11px;line-height:1.35}
  .setup li{margin-bottom:2px}
  .screens{position:absolute;top:182px;left:318px;display:flex;gap:6px}
  .screen{width:86px;height:160px;border:1px solid #ccd;background:linear-gradient(180deg,#3fd0b8 0 10px,var(--mist) 10px)}
  .finding{position:absolute;right:14px;bottom:10px;width:400px;text-align:right}
  .finding p{font-size:10.5px;line-height:1.4}
</style>
</head>
<body>
<div class="spread">

  <section class="page features">
    <svg class="bg" width="600" height="434" viewBox="0 0 600 434">
      <defs>
        <linearGradient id="warm" x1="0" y1="0" x2="1" y2="1">
          <stop offset="0" stop-color="#c9a27a" stop-opacity=".55"/>
          <stop offset=".6" stop-color="#e8e6e2" stop-opacity=".35"/>
          <stop offset="1" stop-color="#6b4328" stop-opacity=".4"/>
        </linearGradient>
      </defs>
      <polygon points="120,0 160,0 0,240 0,180" fill="var(--mist)"/>
      <polygon points="440,0 600,0 600,434 260,434" fill="var(--wood)" role="img" aria-label="Photo of a wooden table with coffee cup, spoon and the Orbo Tag attached to keys"/>
      <polygon points="440,0 600,0 600,434 260,434" fill="url(#warm)"/>
      <polygon points="440,0 464,0 284,434 260,434" fill="var(--blue)" opacity=".85"/>
      <polygon points="540,120 580,120 460,434 420,434" fill="var(--blue)" opacity=".5"/>
      <polygon points="570,0 600,0 600,60 540,220 515,220" fill="var(--blue)" opacity=".35"/>
    </svg>

    <div class="feature-number" style="left:0;top:10px">01</div>
    <svg class="feature-icon" style="left:26px;top:52px" width="70" height="56" viewBox="0 0 70 56">
      <rect x="2" y="12" width="66" height="42" rx="7" fill="var(--blue)"/>
      <rect x="10" y="5" width="14" height="9" rx="2" fill="var(--blue)"/>
      <circle cx="35" cy="33" r="14" fill="var(--paper)"/>
      <circle cx="35" cy="33" r="9" fill="var(--blue-soft)"/>
    </svg>
    <div class="feature-title" style="left:26px;top:128px">Selfie Remote</div>
    <div class="feature-rule" style="left:26px;top:152px;width:120px"></div>
    <p class="feature-text" style="left:26px;top:162px;width:160px">Take group pictures and selfies with the press of a button and store the pics on your phone</p>

    <div class="feature-number" style="left:245px;top:30px">02</div>
    <svg class="feature-icon" style="left:308px;top:44px" width="52" height="70" viewBox="0 0 52 70">
      <path d="M26 68 C26 68 2 40 2 26 A24 24 0 0 1 50 26 C50 40 26 68 26 68Z" fill="var(--blue)"/>
      <circle cx="26" cy="26" r="16" fill="var(--blue-soft)"/>
    </svg>
    <div class="feature-title" style="left:214px;top:128px">Location Record</div>
    <div class="feature-rule" style="left:228px;top:152px;width:120px"></div>
    <p class="feature-text" style="left:180px;top:162px;width:150px;text-align:center">Locate lost items with the Lost Record feature that provides exact coordinates of your last connected location</p>

    <div class="feature-number" style="left:0;top:230px">03</div>
    <svg class="feature-icon" style="left:26px;top:266px" width="84" height="46" viewBox="0 0 84 46">
      <rect x="2" y="2" width="74" height="42" rx="6" fill="var(--blue)"/>
      <rect x="76" y="14" width="6" height="18" rx="2" fill="var(--blue)"/>
      <rect x="9" y="9" width="60" height="28" rx="3" fill="var(--blue-soft)"/>
    </svg>
    <div class="feature-title" style="left:18px;top:334px">Battery Tracking</div>
    <div class="feature-rule" style="left:18px;top:358px;width:140px"></div>
    <p class="feature-text" style="left:18px;top:368px;width:200px">Monitor the Orbo Tag's battery life within the app. Never run out of juice when you need it the most! Our battery can easily be replaced</p>

    <div class="page-heading features-heading">FEATURES</div>
  </section>

  <section class="page application">
    <svg class="bg" width="600" height="434" viewBox="0 0 600 434">
      <defs>
        <linearGradient id="veil" x1="0" y1="0" x2="1" y2="1">
          <stop offset="0" stop-color="#85cae6" stop-opacity=".5"/>
          <stop offset="1" stop-color="#0692cd" stop-opacity=".3"/>
        </linearGradient>
      </defs>
      <polygon points="0,0 390,0 140,434 0,434" fill="var(--blue-deep)" role="img" aria-label="Photo of a coffee cup on a table with the Orbo Tag, under a blue overlay"/>
      <polygon points="0,0 390,0 140,434 0,434" fill="url(#veil)"/>
      <polygon points="310,0 328,0 120,434 102,434" fill="var(--paper)" opacity=".55"/>
      <polygon points="265,0 280,0 72,434 57,434" fill="var(--paper)" opacity=".25"/>
      <polygon points="200,300 216,300 156,434 140,434" fill="var(--paper)" opacity=".7"/>
    </svg>

    <div class="page-heading application-heading">APPLICATION</div>

    <div class="setup">
      <h2>Setting up Orbo Tag</h2>
      <ol>
        <li>1. Download the free "Trakly" app</li>
        <li>2. Turn on the device with a long press</li>
        <li>3. Open the app and press the "+" icon, then select the Orbo Tag device to pair</li>
      </ol>
    </div>

    <div class="screens">
      <div class="screen" role="img" aria-label="App screen: add device"></div>
      <div class="screen" role="img" aria-label="App screen: paired keys device"></div>
      <div class="screen" role="img" aria-label="App screen: tag calling phone"></div>
    </div>

    <div class="finding">
      <h2>Finding your valuables</h2>
      <p>To locate your phone: Double press the finder to activate the alarm on your phone.
      To find your keys or other attached item just go to the "Device" tab, select your connected finder and press the "Call" button</p>
    </div>
  </section>

</div>
</body>
</html>
```